Book Cover Design Project

I need a book cover for a book that we will be releasing in the next few months.

It is a business book aimed at small businesses and people who want to escape the 9 - 5 and start their own business.

We want it to look similar to: http://www.tolvanbrook.example/wp-content/uploads/2010/03/fold-up.jpg and also the book designs that I have uploaded images for.

I quite like the grey / charcoal background and the bright lime green colours from the Quiet Harbor logo that I have attached. However, anything bright would be good - I am prepared to be flexible with colours. The books I have attached are a high impact as well - being bright blue with white black font with a really cool font.

The book is titled:

The Lantern Shop Plan

By Dale Vortan

Still thinking of the tagline, for now just use "Start an Online Business in no time at all"

Room for a quote/testimonial on the front of the book at the bottom, and as well on the back.

For the back cover text just use dummy text and my photo that is attached for now as well.

Barcode ISBN on the back at the bottom - price will be $19.95

Needs to be in PSD so we can change the text from our end.

I really want to get a good template made that I can edit the text for as we are still developing the book, but I want to get the book cover done so I can start advertising that it will be arriving soon.

There will probably be alterations that I need help with later down the track so looking to work with someone closely on this, and I will pay you for any extra time down the track..

Sizes will probably be around: I think 20.5cm tall and 14cm wide would be good..

Not sure how thick for the spine, it will depend on how many words get cut off, but as an estimate probably 1.5CM..
Updates

Just added some more detail to the brief.. Please read it carefully.

Target Market(s)

small business owners, professionals who want to start their own business, soon to be entrepreneurs, entrepreneurs

Industry/Entity Type

Advertising

Requirements
Must have
• The Lantern Shop Plan

and Dale Vortan must be prominent.

Tag line should be look cool under the title.

Must be very modern and cool. Needs to catch people's eyes so needs to be really punchy.

Nice to have
• Maybe a clock or stopwatch icon would be cool to add in there so it isn't just plain.. Similar to like how the books have a cool icon with them that I have attached in the uploaded images.
Should not have
• I like simplicity, artistic and very high impact. It really needs to draw you in and catch your eye.

Don't use plain boring fonts. Although I like simplicity slick design is very important - I dont want it to be boring - it has to look high quality and expensive. Therefore do not use fonts like Arial, Times New Roman those really boring fonts that make it look cheap. If I was going to do something like that then I might as well do it myself.

If you want to see the quality of things that I am usually involved with look at the artwork for one of my events that I run called Daybreaker: http://www.daybreaker.example/daybreaker-festival-anthems-ft-loomsparrow-harvest-night-eve-metro-report/

That will give you an idea of what type of quality things that I am involved with, so you need to be up for the task..

```html
<!DOCTYPE html>
<html lang="en">
<head>
<meta charset="utf-8">
<title>The Lantern Shop Plan — Book Cover</title>
<link rel="stylesheet" href="https://fonts.googleapis.com/css2?family=Oswald:wght@600;700&family=Michroma&family=Archivo:wght@700&display=swap">
<style>
  :root {
    --stage: #ffffff;
    --charcoal-light: #6f6f6f;
    --charcoal: #555555;
    --charcoal-dark: #3e3e3e;
    --lime: #d6e021;
    --white: #ffffff;
    --shadow: rgba(0, 0, 0, 0.45);
  }
  * { box-sizing: border-box; margin: 0; padding: 0; }
  html, body {
    width: 1200px;
    height: 1000px;
    overflow: hidden;
    background: var(--stage);
  }
  .canvas {
    position: relative;
    width: 1200px;
    height: 1000px;
  }
  .cover {
    position: absolute;
    left: 330px;
    top: 60px;
    width: 540px;
    height: 880px;
    overflow: hidden;
    box-shadow: 0 10px 30px rgba(0, 0, 0, 0.18);
  }
  .cover-backdrop {
    position: absolute;
    inset: 0;
    background:
      radial-gradient(circle at 50% 48%, var(--charcoal-light) 0%, var(--charcoal) 45%, transparent 46%),
      radial-gradient(circle at 50% 48%, transparent 50%, rgba(255,255,255,0.05) 51%, transparent 53%),
      linear-gradient(180deg, var(--charcoal-light) 0%, var(--charcoal) 50%, var(--charcoal-dark) 100%);
  }
  .author {
    position: absolute;
    top: 48px;
    left: 0;
    width: 100%;
    padding-left: 130px;
    font-family: "Oswald", sans-serif;
    font-weight: 700;
    font-size: 38px;
    letter-spacing: 1px;
    color: var(--lime);
    text-shadow: 2px 2px 0 var(--shadow);
  }
  .kicker {
    position: absolute;
    top: 150px;
    right: 40px;
    display: flex;
    align-items: center;
  }
  .kicker-streak {
    width: 300px;
    height: 36px;
    margin-right: 4px;
  }
  .kicker-word {
    font-family: "Michroma", sans-serif;
    font-size: 42px;
    line-height: 1;
    color: var(--white);
    letter-spacing: 1px;
    -webkit-text-stroke: 1px var(--white);
  }
  .title {
    position: absolute;
    top: 212px;
    left: 24px;
    width: 480px;
    height: 330px;
    color: var(--lime);
    font-family: "Oswald", sans-serif;
    font-weight: 700;
    text-transform: uppercase;
  }
  .title-article {
    position: absolute;
    left: 0;
    bottom: 20px;
    writing-mode: vertical-rl;
    transform: rotate(180deg);
    font-size: 40px;
    line-height: 1;
    text-shadow: 2px 2px 0 var(--shadow);
  }
  .title-words {
    position: absolute;
    right: 0;
    top: 0;
    width: 432px;
    height: 330px;
    overflow: visible;
    filter: drop-shadow(3px 3px 0 var(--shadow));
  }
  .title-words text {
    fill: var(--lime);
    font-family: "Oswald", sans-serif;
    font-weight: 700;
    font-size: 180px;
  }
  .tagline {
    position: absolute;
    top: 560px;
    left: 0;
    width: 100%;
    text-align: center;
    color: var(--white);
    font-family: "Michroma", sans-serif;
    text-transform: uppercase;
  }
  .tagline-main {
    display: block;
    font-size: 29px;
    line-height: 1.3;
    -webkit-text-stroke: 0.8px var(--white);
  }
  .tagline-sub {
    display: block;
    font-size: 25px;
    line-height: 1.4;
    letter-spacing: 3px;
    -webkit-text-stroke: 0.8px var(--white);
  }
  .testimonial {
    position: absolute;
    top: 712px;
    left: 34px;
    right: 34px;
    font-family: "Archivo", sans-serif;
    font-weight: 700;
    font-size: 13px;
    line-height: 1.75;
    color: var(--white);
    text-align: justify;
  }
  .testimonial-source {
    color: var(--lime);
    font-style: normal;
    margin-left: 6px;
  }
</style>
</head>
<body>
<main class="canvas">
  <article class="cover">
    <div class="cover-backdrop" role="img" aria-label="Charcoal gradient with a faint stopwatch behind the title"></div>

    <p class="author">Dale Vortan</p>

    <div class="kicker">
      <svg class="kicker-streak" viewBox="0 0 300 36" aria-hidden="true">
        <defs>
          <linearGradient id="streak-fade" x1="0" x2="1" y1="0" y2="0">
            <stop offset="0" stop-color="#ffffff" stop-opacity="0"/>
            <stop offset="1" stop-color="#ffffff" stop-opacity="0.85"/>
          </linearGradient>
        </defs>
        <rect x="0" y="2" width="300" height="6" fill="url(#streak-fade)" opacity="0.6"/>
        <rect x="40" y="12" width="260" height="12" fill="url(#streak-fade)"/>
        <rect x="0" y="28" width="300" height="6" fill="url(#streak-fade)" opacity="0.6"/>
      </svg>
      <span class="kicker-word">START</span>
    </div>

    <h1 class="title">
      <span class="title-article">The</span>
      <svg class="title-words" viewBox="0 0 432 330" aria-label="Lantern Shop Plan">
        <text x="0" y="152" textLength="428" lengthAdjust="spacingAndGlyphs">LANTERN</text>
        <text x="0" y="318" textLength="428" lengthAdjust="spacingAndGlyphs">SHOP PLAN</text>
      </svg>
    </h1>

    <p class="tagline">
      <span class="tagline-main">An Online Business</span>
      <span class="tagline-sub">In No Time At All</span>
    </p>

    <blockquote class="testimonial">
      Lorem ipsum dolor sit amet, consectetur adipiscing elit. Duis et mauris metus, eu posuere sem. Nunc nisi neque, cursus in ornare sed, commodo ut mi. Nam metus sem, porta et facilisis non, tristique eget libero. Praesent ornare nisi-<cite class="testimonial-source">NORTHGATE DAILY</cite>
    </blockquote>
  </article>
</main>
</body>
</html>
```